Business Card template - vertical layout

Design a vertical business card template to my exisiting specifications with examples shown.
This is a business card template and I need to flexibility to change the company logo and details myself in future.
The main colour scheme is blue, white, grey.
Clean, professional designs would be appreciated.
Business
The format is double sided, vertical layout as shown in the example image.
The business card is going to be a template design which means I need to be able to change the company logo and details on side B myself in future.
Side A:
company logo with blue background (as shown in the example image, same blue colour)
Side B:
company logo on the top
personal name (Leo Brandt)
job title (Chief Executive Officer)
mobile phone number (+61 455 913 270)
email: (leo.brandt@corvalmedix.com.au)
wechat: (leobrandt8)
PO Box address (PO Box 27415 Melbourne VIC 3001)
Office address: (482 Harwick Street Melbourne VIC 3008 Australia)
office address 2: (Level 2, 7 Tamsin Street Burwood NSW 2134)

```html
<!DOCTYPE html>
<html lang="en">
<head>
<meta charset="utf-8">
<title>Business Card Template – Vertical</title>
<link href="https://fonts.googleapis.com/css2?family=Varela+Round&display=swap" rel="stylesheet">
<style>
  :root {
    --bg: #ececec;
    --blue: #4a78bb;
    --blue-deep: #3a69b0;
    --blue-mid: #6a9bcf;
    --blue-light: #7cc0e6;
    --blue-text: #3f6fb6;
    --green: #8cc152;
    --white: #ffffff;
    --font: "Varela Round", Arial, sans-serif;
  }
  * { margin: 0; padding: 0; box-sizing: border-box; }
  html, body { width: 1200px; height: 875px; overflow: hidden; }
  body {
    background: var(--bg);
    font-family: var(--font);
    position: relative;
  }
  .card {
    position: absolute;
    top: 160px;
    width: 340px;
    height: 556px;
    overflow: hidden;
    background: var(--white);
    box-shadow: 0 6px 18px rgba(0,0,0,0.12);
  }
  .card svg.card-art { position: absolute; inset: 0; }
  .card--front { left: 240px; }
  .card--back { left: 620px; }

  .front-logo {
    position: absolute;
    left: 0; right: 0; top: 245px;
    text-align: center;
    color: var(--white);
    font-size: 52px;
    letter-spacing: 1px;
  }

  .back-logo {
    position: absolute;
    left: 150px; top: 170px;
    color: var(--blue-text);
    font-size: 34px;
  }
  .person { position: absolute; left: 48px; top: 252px; }
  .person__name { color: var(--green); font-size: 32px; line-height: 1; }
  .person__title { color: var(--blue-text); font-size: 12px; margin-top: 4px; }

  .contacts {
    position: absolute;
    left: 30px; top: 322px;
    list-style: none;
    color: var(--blue-text);
    font-size: 13px;
  }
  .contacts li { display: flex; align-items: center; height: 23px; }
  .contacts .icon { width: 15px; height: 15px; margin-right: 9px; flex: none; }
  .addresses {
    position: absolute;
    left: 30px; top: 418px;
    color: var(--blue-text);
    font-size: 13px;
    line-height: 17px;
  }
  .addresses p { margin-bottom: 4px; }
  .website {
    position: absolute;
    left: 0; right: 0; bottom: 14px;
    text-align: center;
    color: var(--white);
    font-size: 14px;
  }
</style>
</head>
<body>

  <!-- Side A -->
  <section class="card card--front" aria-label="Business card, side A">
    <svg class="card-art" width="340" height="556" viewBox="0 0 340 556" aria-hidden="true">
      <defs>
        <linearGradient id="frontBlue" x1="0" y1="0" x2="1" y2="1">
          <stop offset="0" stop-color="#5e8ac6"/>
          <stop offset="0.5" stop-color="#3a69b0"/>
          <stop offset="1" stop-color="#6a93cb"/>
        </linearGradient>
      </defs>
      <path fill="url(#frontBlue)"
        d="M0 70 Q0 14 50 14 L290 14 Q340 14 340 70 L340 486 Q340 542 290 542 L50 542 Q0 542 0 486 Z"/>
    </svg>
    <div class="front-logo">logo here</div>
  </section>

  <!-- Side B -->
  <section class="card card--back" aria-label="Business card, side B">
    <svg class="card-art" width="340" height="556" viewBox="0 0 340 556" aria-hidden="true">
      <rect width="340" height="300" fill="var(--blue)"/>
      <polygon points="0,0 340,0 340,110 0,60" fill="#5e88c4"/>
      <polygon points="0,190 235,67 340,140 340,210" fill="#6fa0d2"/>
      <polygon points="235,67 340,120 340,300 300,260" fill="var(--blue-light)"/>
      <polygon points="0,228 235,67 340,217 340,556 0,556" fill="var(--white)"/>
      <polygon points="0,505 340,520 340,556 0,556" fill="var(--blue-deep)"/>
      <polygon points="0,490 40,508 0,525" fill="#5aa6d8"/>
      <polygon points="290,540 340,522 340,556 300,556" fill="#5aa6d8"/>
    </svg>

    <div class="back-logo">logo here</div>

    <div class="person">
      <div class="person__name">Leo Brandt</div>
      <div class="person__title">Chief Executive Officer</div>
    </div>

    <ul class="contacts">
      <li>
        <svg class="icon" viewBox="0 0 16 16" aria-hidden="true">
          <circle cx="8" cy="8" r="8" fill="var(--green)"/>
          <path d="M5.2 4.2 L6.6 4 L7.3 6 L6.4 6.8 Q7.2 8.6 9.2 9.6 L10 8.7 L12 9.4 L11.8 10.8 Q8 11.6 4.8 7.8 Q4.4 5.4 5.2 4.2 Z" fill="var(--white)"/>
        </svg>+61 455 913 270
      </li>
      <li>
        <svg class="icon" viewBox="0 0 16 16" aria-hidden="true">
          <rect x="1" y="3.5" width="14" height="9" fill="var(--green)"/>
          <path d="M1 3.5 L8 9 L15 3.5" fill="none" stroke="var(--white)" stroke-width="1.2"/>
        </svg>leo.brandt@corvalmedix.com.au
      </li>
      <li>
        <svg class="icon" viewBox="0 0 16 16" aria-hidden="true">
          <circle cx="8" cy="8" r="6.5" fill="var(--green)"/>
        </svg>leobrandt8
      </li>
      <li>
        <svg class="icon" viewBox="0 0 16 16" aria-hidden="true">
          <path d="M8 1.5 L15 8 L13 8 L13 14.5 L9.6 14.5 L9.6 10.5 L6.4 10.5 L6.4 14.5 L3 14.5 L3 8 L1 8 Z" fill="var(--green)"/>
        </svg>PO Box 27415 Melbourne VIC 3001
      </li>
    </ul>

    <div class="addresses">
      <p>482 Harwick Street Melbourne<br>VIC 3008 Australia</p>
      <p>Level 2, 7 Tamsin Street Burwood<br>NSW 2134</p>
    </div>

    <div class="website">www.corvalmedix.com</div>
  </section>

</body>
</html>
```